Best local air conditioning and heating contractor

We need a website design for a new company in Tampa Bay called the Summit Breeze Cooling Company. We provide superior services for residential and commercial properties as well as maintenance and installing HVAC systems. We also want to sell equipment, parts and filter on the website as well. We want it easy to use for customers. Rich with content and keywords for our area.

Target Market(s)

homeowners in Tampa Bay

Industry/Entity Type

HVAC air conditioning and heating

Coding

Coded - Design and coding required

Number of Pages Required

5+ page

Font styles to use
Sans Serif

Requirements
Nice to have
• would like the colors to be same as logo

```html
<!DOCTYPE html>
<html lang="en">
<head>
<meta charset="utf-8">
<title>Summit Breeze Cooling Company – HVAC Contractors in Tampa Bay</title>
<link href="https://fonts.googleapis.com/css2?family=Poppins:wght@400;500;600;700&display=swap" rel="stylesheet">
<style>
:root{
  --navy:#1f2a6b;
  --navy-deep:#141c4d;
  --red:#d9232a;
  --white:#ffffff;
  --ink:#222;
  --grey:#6d6d75;
  --footer:#0b0b0f;
  --line:#cfcfd4;
}
*{box-sizing:border-box;margin:0;padding:0}
html,body{width:1200px;height:3752px;overflow:hidden}
body{font-family:'Poppins',sans-serif;color:var(--ink);background:var(--white);position:relative}
.abs{position:absolute}
a{color:inherit;text-decoration:none}
.bg{position:absolute;inset:0}

/* top bar */
.topbar{left:0;top:0;width:1200px;height:41px;background:var(--navy)}
.topbar .contact{top:10px;font-size:16px;line-height:20px;color:var(--white);display:flex;align-items:center;gap:10px;white-space:nowrap}
.topbar .social{right:50px;top:12px;display:flex;gap:14px}
.topbar .social span{width:16px;height:16px;border-radius:50%;background:var(--white);display:block}

/* nav */
.nav{left:0;top:41px;width:1200px;height:100px;background:var(--white);border-bottom:1px solid #e6e6ea}
.nav a{position:absolute;top:44px;font-size:18px;font-weight:500;color:#333;letter-spacing:.3px}
.nav a.active{color:var(--red)}
.brand{left:468px;top:24px;width:220px;text-align:center;font-weight:700;color:var(--navy);font-size:21px;line-height:26px;text-transform:uppercase}

/* hero */
.hero{left:0;top:141px;width:1200px;height:763px;background:linear-gradient(120deg,#565e88 0%,#7d84a8 45%,#8f95b8 70%,#6c739b 100%)}
.hero-title{left:42px;top:321px;font-size:46px;line-height:54px;font-weight:700;color:var(--white);text-transform:uppercase}
.hero-text{left:42px;top:506px;font-size:19px;line-height:24px;color:var(--white)}
.btn{display:flex;align-items:center;justify-content:center;color:var(--white);font-weight:500;text-transform:uppercase}
.btn-navy{background:var(--navy)}
.btn-red{background:var(--red)}
.quote{left:689px;top:258px;width:444px;height:554px;background:var(--white);border-top-right-radius:110px}
.quote h2{position:absolute;left:61px;top:58px;font-size:24px;line-height:30px;font-weight:500;color:var(--navy);text-transform:uppercase}
.quote .field{position:absolute;left:54px;width:330px;height:58px;border:2px solid var(--line);padding-left:26px;display:flex;align-items:center;font-size:18px;color:#333}

/* about */
.about-img-a{left:92px;top:1048px;width:367px;height:421px;background:linear-gradient(160deg,#c8ccd4,#7e8aa8 55%,#3e4a6e)}
.about-img-b{left:341px;top:1271px;width:224px;height:281px;background:linear-gradient(150deg,#b7b4b0,#d6c3a6 60%,#9c8f82);border:2px solid var(--white)}
.section-title{font-size:29px;font-weight:600;color:var(--navy);text-transform:uppercase}
.about-text{left:652px;width:480px;font-size:16px;line-height:19.5px;color:var(--grey)}

/* services */
.services{left:0;top:1661px;width:1200px;height:641px}
.services .bg{background:linear-gradient(180deg,#4a5380 0%,#5b638c 50%,#474f7a 100%)}
.services h2{position:absolute;left:0;width:1200px;top:78px;text-align:center;font-size:28px;font-weight:600;color:var(--white);text-transform:uppercase}
.card{top:1866px;width:230px;height:327px;background:var(--white)}
.card .photo{height:168px}
.card h3{position:absolute;left:18px;top:200px;font-size:15px;font-weight:600;color:var(--navy)}
.card p{position:absolute;left:20px;top:228px;width:195px;font-size:10.5px;line-height:13px;color:var(--grey)}
.card .more{position:absolute;left:18px;top:280px;font-size:10px;font-weight:600;color:var(--red)}

/* testimonials */
.tcard{top:2497px;width:316px;height:157px;background:var(--white);box-shadow:0 8px 30px rgba(0,0,0,.08);padding:42px 22px 0 22px;font-size:14px;line-height:20.5px;color:var(--grey)}
.author{top:2685px;display:flex;align-items:center;gap:16px}
.author .avatar{width:60px;height:60px;border-radius:50%;background:linear-gradient(135deg,#c9b9a5,#6c6f86)}
.author .name{font-size:15px;font-weight:500;color:var(--navy)}
.author .role{font-size:11px;color:var(--red);text-transform:uppercase;margin-top:2px}

/* call to action */
.cta{left:0;top:2864px;width:1200px;height:453px}
.cta .bg{background:linear-gradient(180deg,#3f4876 0%,#55608c 55%,#2e3661 100%)}
.cta h2{position:absolute;left:178px;top:104px;font-size:29px;line-height:36px;font-weight:600;color:var(--white);text-transform:uppercase}
.cta p{position:absolute;left:181px;top:192px;width:500px;font-size:19px;line-height:26px;color:var(--white)}
.cta .phone{position:absolute;left:189px;top:300px;display:flex;align-items:center;gap:14px;font-size:29px;font-weight:500;color:var(--white)}
.cta .worker{position:absolute;left:743px;top:26px;width:291px;height:427px;background:linear-gradient(180deg,#c8b49c 0%,#6b7a8e 45%,#2f4b5e 70%,#c9963e 100%);border-radius:120px 120px 0 0}

/* footer */
.footer{left:0;top:3317px;width:1200px;height:389px;background:var(--footer);color:var(--white)}
.footer .brand-foot{position:absolute;left:62px;top:150px;width:240px;font-size:22px;line-height:28px;font-weight:700;color:var(--red);text-transform:uppercase}
.footer .divider{position:absolute;top:148px;width:2px;height:125px;background:#cfcfd4}
.footer h4{position:absolute;top:132px;font-size:23px;font-weight:500}
.footer a{position:absolute;font-size:17px}
.footer .email{position:absolute;left:950px;top:179px;width:179px;height:36px;background:var(--white);color:#888;font-size:17px;padding-left:12px;display:flex;align-items:center}
.footer .signup{position:absolute;left:950px;top:230px;width:179px;height:37px;font-size:18px}
.copyright{left:0;top:3706px;width:1200px;height:46px;background:var(--red);color:var(--white);font-size:12px;display:flex;align-items:center;justify-content:center}
</style>
</head>
<body>

<!-- top bar -->
<div class="abs topbar">
  <div class="abs contact" style="left:50px">
    <svg width="16" height="12" viewBox="0 0 16 12"><rect x="0.5" y="0.5" width="15" height="11" fill="#fff"/><path d="M1 1l7 6 7-6" stroke="#1f2a6b" stroke-width="1.4" fill="none"/></svg>
    <span>info@sbcooling.com</span>
  </div>
  <div class="abs contact" style="left:281px">
    <svg width="16" height="16" viewBox="0 0 24 24"><path fill="#fff" d="M6.6 10.8a15 15 0 0 0 6.6 6.6l2.2-2.2c.3-.3.7-.4 1-.2 1.1.4 2.3.6 3.6.6.6 0 1 .4 1 1V20c0 .6-.4 1-1 1A17 17 0 0 1 3 4c0-.6.4-1 1-1h3.5c.6 0 1 .4 1 1 0 1.3.2 2.5.6 3.6.1.3 0 .7-.2 1z"/></svg>
    <span>(555) 014 2290</span>
  </div>
  <div class="abs social"><span></span><span></span><span></span></div>
</div>

<!-- navigation -->
<nav class="abs nav">
  <a class="active" style="left:51px">HOME</a>
  <a style="left:169px">ABOUT</a>
  <a style="left:300px">SERVICES</a>
  <div class="abs brand">Summit Breeze<br>Cooling Company</div>
  <a style="left:756px">PRODUCTS</a>
  <a style="left:922px">FINANCING</a>
  <a style="left:1085px">BLOG</a>
</nav>

<!-- hero -->
<section class="abs hero" role="img" aria-label="Technician installing a ceiling air conditioning unit, tinted navy"></section>
<h1 class="abs hero-title">Heating and air<br>conditioning<br>contractors</h1>
<p class="abs hero-text">Lorem ipsum dolor sit amet, consectetuer adipiscing elit.<br>Aenean commodo ligula eget dolor.<br>&nbsp;Aenean massa.</p>
<a class="abs btn btn-navy" style="left:51px;top:611px;width:175px;height:37px;font-size:16px">Our services</a>
<a class="abs btn btn-red" style="left:249px;top:611px;width:175px;height:37px;font-size:16px">Our products</a>

<form class="abs quote">
  <h2>Air conditioning and<br>heating contractor<br>in Tampa Bay</h2>
  <div class="field" style="top:188px">NAME</div>
  <div class="field" style="top:276px">EMAIL</div>
  <div class="field" style="top:365px">PHONE</div>
  <div class="abs btn btn-red" style="left:131px;top:471px;width:174px;height:37px;font-size:16px;font-weight:400">Get a quote</div>
</form>

<!-- about -->
<div class="abs about-img-a" role="img" aria-label="Two technicians in hard hats inspecting a ceiling vent"></div>
<div class="abs about-img-b" role="img" aria-label="Technician servicing a wall-mounted air conditioner"></div>
<h2 class="abs section-title" style="left:648px;top:1130px">About us</h2>
<p class="abs about-text" style="top:1192px">Lorem ipsum dolor sit amet, consectetuer adipiscing elit. Aenean commodo ligula eget dolor.<br>Aenean massa. Cum sociis natoque penatibus et magnis dis parturient montes, nascetur ridiculus mus.</p>
<p class="abs about-text" style="top:1278px">Lorem ipsum dolor sit amet, consectetuer adipiscing elit. Aenean commodo ligula eget dolor.<br>Aenean massa. Cum sociis natoque penatibus et magnis dis parturient montes, nascetur ridiculus mus.</p>
<a class="abs btn btn-red" style="left:652px;top:1393px;width:191px;height:47px;font-size:19px;font-weight:400">Read more</a>

<!-- services -->
<section class="abs services">
  <div class="bg" role="img" aria-label="Technicians working on a ceiling duct, tinted navy"></div>
  <h2>Superior services in Tampa Bay</h2>
</section>
<article class="abs card" style="left:55px">
  <div class="photo" role="img" aria-label="Family relaxing on a sofa under a wall air conditioner" style="background:linear-gradient(160deg,#e7e3dc,#b9ab96 60%,#6f7a62)"></div>
  <h3>Residential Properties</h3>
  <p>Lorem ipsum dolor sit amet, consectetur adipiscing elit. Ut elit tellus, luctus.</p>
  <span class="more">READ MORE</span>
</article>
<article class="abs card" style="left:338px">
  <div class="photo" role="img" aria-label="Technicians in hard hats inspecting a ceiling unit" style="background:linear-gradient(160deg,#d2d5da,#7e8aa8 55%,#3e4a6e)"></div>
  <h3>Commercial Properties</h3>
  <p>Lorem ipsum dolor sit amet, consectetur adipiscing elit. Ut elit tellus, luctus.</p>
  <span class="more">READ MORE</span>
</article>
<article class="abs card" style="left:622px">
  <div class="photo" role="img" aria-label="Technician servicing an outdoor condenser unit" style="background:linear-gradient(160deg,#8a8c92,#cfd1d4 55%,#5b5f68)"></div>
  <h3>Maintenance</h3>
  <p>Lorem ipsum dolor sit amet, consectetur adipiscing elit. Ut elit tellus, luctus.</p>
  <span class="more">READ MORE</span>
</article>
<article class="abs card" style="left:903px">
  <div class="photo" role="img" aria-label="Technician installing an indoor unit" style="background:linear-gradient(160deg,#a9a6a3,#d8c8b2 55%,#8e8a86)"></div>
  <h3>Installation</h3>
  <p>Lorem ipsum dolor sit amet, consectetur adipiscing elit. Ut elit tellus, luctus.</p>
  <span class="more">READ MORE</span>
</article>

<!-- testimonials -->
<h2 class="abs section-title" style="left:0;width:1180px;text-align:center;top:2382px">What customer say’s</h2>
<blockquote class="abs tcard" style="left:76px">Egestas fringilla phasellus faucibus scelerisque. Massa tincidunt dui ut ornare lectus. Elit ullamcorper dignissim cras tincidunt lobortis feugiat vivamus at.</blockquote>
<blockquote class="abs tcard" style="left:437px">Egestas fringilla phasellus faucibus scelerisque. Massa tincidunt dui ut ornare lectus. Elit ullamcorper dignissim cras tincidunt lobortis feugiat vivamus at.</blockquote>
<blockquote class="abs tcard" style="left:798px">Egestas fringilla phasellus faucibus scelerisque. Massa tincidunt dui ut ornare lectus. Elit ullamcorper dignissim cras tincidunt lobortis feugiat vivamus at.</blockquote>
<div class="abs author" style="left:94px"><div class="avatar" role="img" aria-label="Customer portrait"></div><div><div class="name">Dana R. Whitfield</div><div class="role">Customer</div></div></div>
<div class="abs author" style="left:447px"><div class="avatar" role="img" aria-label="Customer portrait"></div><div><div class="name">Dana R. Whitfield</div><div class="role">Customer</div></div></div>
<div class="abs author" style="left:815px"><div class="avatar" role="img" aria-label="Customer portrait"></div><div><div class="name">Dana R. Whitfield</div><div class="role">Customer</div></div></div>

<!-- call to action -->
<section class="abs cta">
  <div class="bg" role="img" aria-label="Tampa Bay waterfront skyline, tinted navy"></div>
  <h2>Need professional HVAC<br>contractors in Tampa Bay?</h2>
  <p>Egestas fringilla phasellus faucibus scelerisque. Massa tincidunt dui ut ornare lectus. Elit ullamcorper dignissim cras tincidunt lobortis feugiat vivamus at.</p>
  <div class="phone">
    <svg width="60" height="60" viewBox="0 0 60 60"><circle cx="30" cy="30" r="27" fill="none" stroke="#fff" stroke-width="3"/><path fill="none" stroke="#fff" stroke-width="3" stroke-linejoin="round" d="M20 17l6 0 3 8-4 3a18 18 0 0 0 7 7l3-4 8 3 0 6c0 2-2 3-4 3A24 24 0 0 1 17 21c0-2 1-4 3-4z"/></svg>
    <span>555 017 6789</span>
  </div>
  <div class="worker" role="img" aria-label="Smiling HVAC technician holding a wrench, wearing a plaid shirt and tool belt"></div>
</section>

<!-- footer -->
<footer class="abs footer">
  <div class="brand-foot">Summit Breeze<br>Cooling Company</div>
  <span class="divider" style="left:350px"></span>
  <h4 style="left:390px">Explore</h4>
  <a style="left:390px;top:170px">Home</a>
  <a style="left:390px;top:214px">About</a>
  <a style="left:390px;top:259px">Services</a>
  <a style="left:526px;top:172px">Products</a>
  <a style="left:526px;top:214px">Testimonials</a>
  <a style="left:529px;top:259px">Contact</a>
  <h4 style="left:714px">Quick Links</h4>
  <a style="left:714px;top:175px">Privacy Policy</a>
  <a style="left:716px;top:212px">Terms &amp; Conditions</a>
  <a style="left:719px;top:250px">Cokkies Policy</a>
  <span class="divider" style="left:902px"></span>
  <h4 style="left:950px">Newsletter</h4>
  <div class="email">Email Address</div>
  <div class="btn btn-red signup">Signup now</div>
</footer>
<div class="abs copyright">Privacy Policy | © Copyright Summit Breeze 2022 |</div>

</body>
</html>
```